Business Card/Letterhead Design

We have our Logo, we simply need it cleaned up. Along with a letterhead design. It's pretty simple really.
Instead of the "Corporation" beside the logo. We need it to say "Limited" just under the logo between the "F" and the "Y"
The letter head has to have our address. 4375 Calverton Road Mississauga, ON L4W 2K7 Canada
Updates
Reason: I have been called out of town until Monday of next week.
Industry/Entity Type
Business
Contact Information for Business Card
4375 Calverton Road Mississauga, ON L4W 2K7 Canada
Look and feel
Each slider illustrates characteristics of the customer's brand and the style your logo design should communicate.

```html
<!DOCTYPE html>
<html lang="en">
<head>
<meta charset="utf-8">
<title>Alderbrook Limited – Business Card</title>
<link rel="stylesheet" href="https://fonts.googleapis.com/css2?family=Source+Sans+3:wght@400;600&display=swap">
<style>
  :root {
    --brand-blue: #4b4aa6;
    --brand-tan: #bf956c;
    --ink: #2c2c2c;
    --card: #ffffff;
    --backdrop: #e9e7e3;
  }
  * { margin: 0; padding: 0; box-sizing: border-box; }
  html, body { width: 1200px; height: 1200px; overflow: hidden; }
  body {
    background: var(--backdrop);
    font-family: "Source Sans 3", "Myriad Pro", Arial, sans-serif;
    color: var(--ink);
  }
  .sheet {
    width: 1200px; height: 1200px;
    display: flex; flex-direction: column;
    align-items: center; justify-content: center; gap: 60px;
  }
  .card {
    position: relative;
    width: 900px; height: 514px;
    background: var(--card);
    box-shadow: 0 4px 16px rgba(0,0,0,0.12);
    overflow: hidden;
  }
  .company-name {
    position: absolute;
    font-size: 54px; font-weight: 400; line-height: 1;
    color: var(--brand-blue); white-space: nowrap;
  }
  .card-front .company-name { left: 50%; top: 50%; transform: translate(-50%, -50%); }
  .card-back .company-name { left: 600px; top: 228px; transform: translateX(-50%); font-size: 44px; }

  .corner-mark { position: absolute; left: 0; top: 22px; }
  .holder { position: absolute; left: 66px; top: 22px; }
  .holder-name { font-size: 34px; font-weight: 600; color: var(--brand-blue); line-height: 1.1; }
  .holder-title { font-size: 20px; color: var(--ink); }

  .contact {
    position: absolute; left: 40px; top: 215px;
    font-size: 19px; line-height: 1.35; list-style: none;
  }
  .contact .gap { margin-top: 12px; }
  .contact .label { color: var(--brand-blue); }
  .bands { position: absolute; left: 0; bottom: 0; }
</style>
</head>
<body>
<main class="sheet">
  <section class="card card-front" aria-label="Card front">
    <p class="company-name">Alderbrook Limited</p>
  </section>

  <section class="card card-back" aria-label="Card back">
    <svg class="corner-mark" width="56" height="44" viewBox="0 0 56 44" aria-hidden="true">
      <polygon points="0,0 56,0 36,30 0,30" fill="var(--brand-blue)"/>
      <polygon points="36,30 56,0 56,44 0,44 0,30" fill="var(--brand-tan)"/>
    </svg>
    <div class="holder">
      <p class="holder-name">Daniel Reeve</p>
      <p class="holder-title">Managing Director</p>
    </div>
    <ul class="contact">
      <li>12345, Address Goes Here</li>
      <li>Country Name, 123456</li>
      <li class="gap"><span class="label">p:</span> 044-555 010 234</li>
      <li><span class="label">f:</span> 044-555 010 234</li>
      <li><span class="label">e:</span> info@alderbrookltd.com</li>
    </ul>
    <p class="company-name">Alderbrook Limited</p>
    <svg class="bands" width="900" height="120" viewBox="0 0 900 120" aria-hidden="true">
      <polygon points="0,0 400,0 420,28 0,28" fill="var(--brand-blue)"/>
      <polygon points="400,20 900,20 900,120 480,120" fill="var(--brand-tan)"/>
    </svg>
  </section>
</main>
</body>
</html>
```